Designing a Chocolate Bar's Package

We are a chocolate manufacturing company located in Lebanon. We produce chocolate on a wholesale level, and we are planning a new line of production at the moment.
We intend to be make small chocolate bars (about 30g) similar to the "Varmo Radiance" bar with several flavors. 2 flavors have been decided so far (Mint flavored dark chocolate and Plain dark chocolate).
The packaging material will be similar to varmo's package as well. It won't be a carton box. It'll be some sort of paper wrapping the entire bar. So I am looking for a design that has a unique and cool front and back look.
If only one design is to be prepared, please choose either the mint's flavor or the plain dark chocolate, and prepare the design accordingly.
Updates
Project Deadline Extended
Reason: I still have some time to begin the production. The new deadline,therefore, is the end of this month.
Target Market(s)
basically all chocolate lovers...
Industry/Entity Type
It Company
Requirements
Must have
- I will be uploading our logo. Please make sure to use it in the design.

```html
<!DOCTYPE html>
<html lang="en">
<head>
<meta charset="utf-8">
<title>Corvella – Artisan Chocolate Bar Range</title>
<link href="https://fonts.googleapis.com/css2?family=Great+Vibes&family=Arimo:wght@400;700&display=swap" rel="stylesheet">
<style>
  :root {
    --page: #ffffff;
    --wrapper: #000000;
    --pod-tone: #202020;
    --brand-brown: #5b3a20;
    --white: #ffffff;
    --mint: #2fb573;
    --dark: #c0202e;
    --milk: #8fb4e0;
    --orange: #f7941d;
  }
  * { margin: 0; padding: 0; box-sizing: border-box; }
  html, body { width: 1200px; height: 848px; overflow: hidden; background: var(--page); }
  .sheet { position: relative; width: 1200px; height: 848px; }

  .store-brand { position: absolute; left: 60px; top: 88px; color: var(--brand-brown); }
  .store-brand__name { font-family: "Great Vibes", cursive; font-size: 68px; line-height: 1; }
  .store-brand__tagline { font-family: "Great Vibes", cursive; font-size: 17px; margin-left: 18px; margin-top: -4px; }

  .bar {
    position: absolute; top: 288px; width: 205px; height: 460px;
    background: var(--wrapper); overflow: hidden;
    box-shadow: 6px 6px 7px rgba(0,0,0,.45);
    color: var(--white); text-align: center;
  }
  .bar--mint { left: 164px; --accent: var(--mint); }
  .bar--dark { left: 407px; --accent: var(--dark); }
  .bar--milk { left: 644px; --accent: var(--milk); }
  .bar--orange { left: 884px; --accent: var(--orange); }

  .bar__brand {
    position: absolute; top: 50px; left: 0; right: 0;
    font-family: "Great Vibes", cursive; font-size: 44px; line-height: 1;
    color: var(--accent);
  }
  .bar__band {
    position: absolute; top: 136px; left: 0; right: 0; height: 110px;
    background: var(--accent); overflow: hidden;
  }
  .bar__flavour {
    position: absolute; top: 8px; left: 50%; transform: translateX(-50%);
    font-family: Arimo, Arial, sans-serif; font-weight: 700; font-size: 42px;
    letter-spacing: 2px; line-height: 1; white-space: nowrap;
    color: rgba(255,255,255,.35);
  }
  .bar__chocolate {
    position: absolute; top: 32px; left: 0; right: 0;
    font-family: "Great Vibes", cursive; font-size: 34px; line-height: 1;
  }
  .bar__description {
    position: absolute; top: 73px; left: 0; right: 0;
    font-family: Arimo, Arial, sans-serif; font-size: 11px; line-height: 1.3;
  }
  .bar__pod {
    position: absolute; top: 256px; left: 0; right: 0; height: 122px;
    background: radial-gradient(ellipse at center, var(--pod-tone) 0%, #0c0c0c 60%, var(--wrapper) 100%);
  }
  .bar__weight {
    position: absolute; top: 424px; left: 0; right: 0;
    font-family: Arimo, Arial, sans-serif; font-size: 18px;
  }
  .bar__range {
    position: absolute; bottom: 3px; left: 0; right: 0;
    font-family: Arimo, Arial, sans-serif; font-weight: 700; font-size: 15px;
    letter-spacing: .5px; white-space: nowrap;
  }
  .bar__range-accent { color: var(--accent); }
</style>
</head>
<body>
<main class="sheet">
  <header class="store-brand">
    <div class="store-brand__name">Corvella</div>
    <div class="store-brand__tagline">Quality Chocolate Store</div>
  </header>

  <article class="bar bar--mint">
    <div class="bar__brand">Corvella</div>
    <div class="bar__band">
      <div class="bar__flavour">MINT</div>
      <div class="bar__chocolate">chocolate</div>
      <p class="bar__description">rich dark chocolate<br>infused with a subtle mint</p>
    </div>
    <div class="bar__pod" role="img" aria-label="Faint line drawing of cocoa pods and beans"></div>
    <div class="bar__weight">30g</div>
    <div class="bar__range"><span class="bar__range-accent">ARTISAN</span> CHOCOLATE</div>
  </article>

  <article class="bar bar--dark">
    <div class="bar__brand">Corvella</div>
    <div class="bar__band">
      <div class="bar__flavour">DARK</div>
      <div class="bar__chocolate">chocolate</div>
      <p class="bar__description">rich dark chocolate<br>68% cacoa</p>
    </div>
    <div class="bar__pod" role="img" aria-label="Faint line drawing of cocoa pods and beans"></div>
    <div class="bar__weight">30g</div>
    <div class="bar__range"><span class="bar__range-accent">ARTISAN</span> CHOCOLATE</div>
  </article>

  <article class="bar bar--milk">
    <div class="bar__brand">Corvella</div>
    <div class="bar__band">
      <div class="bar__flavour">MILK</div>
      <div class="bar__chocolate">chocolate</div>
      <p class="bar__description">creamy milk chocolate<br>with a hint of sea salt</p>
    </div>
    <div class="bar__pod" role="img" aria-label="Faint line drawing of cocoa pods and beans"></div>
    <div class="bar__weight">30g</div>
    <div class="bar__range"><span class="bar__range-accent">ARTISAN</span> CHOCOLATE</div>
  </article>

  <article class="bar bar--orange">
    <div class="bar__brand">Corvella</div>
    <div class="bar__band">
      <div class="bar__flavour">ORANGE</div>
      <div class="bar__chocolate">chocolate</div>
      <p class="bar__description">rich dark chocolate<br>infused with a sicilian orange oil</p>
    </div>
    <div class="bar__pod" role="img" aria-label="Faint line drawing of cocoa pods and beans"></div>
    <div class="bar__weight">30g</div>
    <div class="bar__range"><span class="bar__range-accent">ARTISAN</span> CHOCOLATE</div>
  </article>
</main>
</body>
</html>
```